AUSTRALIAN CONSULTING FIRM BUSINESS CARD - MODERN

We are wanting a modern, clean lined business card design. We are professional niche consultancy firm situated in Australia called Marlow Advisory Partners Pty Ltd.
The card should communicate professionalism and creativity and draw on our logo design (attached).
The design should be two sided, landscape orientation.
Target Market(s)
government, not for profit sector, corporate clients
Industry/Entity Type
Landscape
Requirements
Must have
- logo
no new introduced colours

```html
<!DOCTYPE html>
<html lang="en">
<head>
<meta charset="utf-8">
<title>Marlow Advisory Partners – Business Card</title>
<link rel="stylesheet" href="https://fonts.googleapis.com/css2?family=Quicksand:wght@400;500;700&display=swap">
<style>
  :root {
    --bg: #e9eaec;
    --card: #ffffff;
    --navy: #2b3d8f;
    --blue: #1ba6df;
    --purple: #9b4f9f;
    --green: #a2c64a;
    --ink: #2a2a2a;
    --rule: #c9c9c9;
  }
  * { box-sizing: border-box; margin: 0; padding: 0; }
  html, body {
    width: 1200px; height: 873px; overflow: hidden;
    background: var(--bg);
    font-family: "Quicksand", sans-serif;
  }
  .stage {
    width: 1200px; height: 873px;
    display: flex; align-items: center; justify-content: center; gap: 60px;
  }
  .card {
    position: relative;
    width: 520px; height: 300px;
    background: var(--card);
    box-shadow: 0 2px 10px rgba(0,0,0,.12);
    overflow: hidden;
  }

  /* Front: brand + contact */
  .front .brand-area {
    position: absolute; left: 0; top: 0; width: 220px; height: 100%;
    display: flex; align-items: center; justify-content: center;
  }
  .front .divider {
    position: absolute; left: 220px; top: 40px; bottom: 40px;
    width: 1px; background: var(--rule);
  }
  .brand-name {
    display: flex; align-items: center; gap: 10px;
    color: var(--navy); font-weight: 700;
  }
  .brand-name .dot {
    width: 14px; height: 14px; border-radius: 50%; background: var(--blue); flex: none;
  }
  .front .brand-name { font-size: 18px; line-height: 1.2; max-width: 180px; }

  .contact { position: absolute; left: 250px; right: 0; top: 50px; }
  .holder {
    display: flex; align-items: center; gap: 8px;
    font-size: 18px; font-weight: 700; color: var(--ink);
    margin-bottom: 18px;
  }
  .holder svg { width: 16px; height: 16px; fill: var(--ink); }
  .band {
    display: flex; align-items: center; gap: 12px;
    height: 44px; padding-left: 16px;
    color: #fff; font-size: 14px; font-weight: 500;
  }
  .band svg { width: 16px; height: 16px; fill: #fff; flex: none; }
  .band-email { background: var(--blue); }
  .band-address { background: var(--purple); }
  .band-address b { font-weight: 700; }
  .band-phone { background: var(--green); }

  /* Back: brand centred + edge strip */
  .back .edge-strip {
    position: absolute; left: 0; top: 0; width: 16px; height: 100%;
    display: flex; flex-direction: column-reverse;
  }
  .edge-strip span { flex: 1; }
  .edge-strip .s-green { background: var(--green); }
  .edge-strip .s-purple { background: var(--purple); }
  .edge-strip .s-blue { background: var(--blue); }
  .back .brand-area {
    position: absolute; inset: 0;
    display: flex; align-items: center; justify-content: center;
  }
  .back .brand-name { font-size: 22px; }
</style>
</head>
<body>
<main class="stage">

  <section class="card front" aria-label="Business card front">
    <div class="brand-area">
      <div class="brand-name"><span class="dot"></span><span>Marlow Advisory Partners Pty Ltd</span></div>
    </div>
    <div class="divider"></div>
    <div class="contact">
      <p class="holder">
        <svg viewBox="0 0 16 16" aria-hidden="true"><circle cx="8" cy="4" r="3.2"/><path d="M1.5 16c0-4 2.9-6.5 6.5-6.5s6.5 2.5 6.5 6.5z"/></svg>
        Sample Name
      </p>
      <p class="band band-email">
        <svg viewBox="0 0 16 16" aria-hidden="true"><path d="M1 3h14v10H1z" fill="none" stroke="#fff" stroke-width="1.4"/><path d="M1 3l7 6 7-6" fill="none" stroke="#fff" stroke-width="1.4"/></svg>
        hello@marlowadvisory.com
      </p>
      <p class="band band-address">
        <svg viewBox="0 0 16 16" aria-hidden="true"><path d="M8 0.5a5.5 5.5 0 0 0-5.5 5.5C2.5 10 8 15.5 8 15.5S13.5 10 13.5 6A5.5 5.5 0 0 0 8 .5zm0 7.8a2.3 2.3 0 1 1 0-4.6 2.3 2.3 0 0 1 0 4.6z"/></svg>
        <span>418 Harbour Lane Kew <b>3101</b></span>
      </p>
      <p class="band band-phone">
        <svg viewBox="0 0 16 16" aria-hidden="true"><path d="M3.6 1l2.6 3.2-1.6 1.8c.9 2 2.4 3.5 4.4 4.4l1.8-1.6L14 11.4 12.6 14.5C6.6 14.3 1.7 9.4 1.5 3.4z"/></svg>
        (03) 9555 0148
      </p>
    </div>
  </section>

  <section class="card back" aria-label="Business card back">
    <div class="edge-strip"><span class="s-green"></span><span class="s-purple"></span><span class="s-blue"></span></div>
    <div class="brand-area">
      <div class="brand-name"><span class="dot"></span><span>Marlow Advisory Partners Pty Ltd</span></div>
    </div>
  </section>

</main>
</body>
</html>
```